LOGO for A Neighborhood Finance Center
BLUE LEDGER PLUS
Professional
HAROLD QUINCE and DENNIS HOLTBERG
Manger
3710 S Wexford st 204
Ashcombe GA 30999
BlueLEDGERPLUS@mailnook.example
BLUELEDGERPLUS.example
I need two versions one with Harold Quince
I need one with Dennis Holtberg

```html
<!DOCTYPE html>
<html lang="en">
<head>
<meta charset="utf-8">
<title>Blue Ledger Plus – Business Cards</title>
<link rel="stylesheet" href="https://fonts.googleapis.com/css2?family=Montserrat:wght@400;600;700&display=swap">
<style>
  :root {
    --backdrop: #d9dcdf;
    --card-dark: #0d0d0f;
    --card-light: #ffffff;
    --brand-green: #7cc242;
    --brand-blue: #1c6db3;
    --brand-teal: #1a9aa8;
    --text-light: #ffffff;
    --text-dark: #222326;
  }
  * { box-sizing: border-box; margin: 0; padding: 0; }
  html, body { width: 1200px; height: 732px; overflow: hidden; }
  body {
    background: var(--backdrop);
    font-family: "Montserrat", Arial, sans-serif;
    position: relative;
  }
  .card {
    position: absolute;
    width: 532px;
    height: 290px;
    border-radius: 22px;
    overflow: hidden;
    box-shadow: 0 6px 14px rgba(0,0,0,0.25);
  }
  .card--dark { background: var(--card-dark); color: var(--text-light); }
  .card--light { background: var(--card-light); color: var(--text-dark); }
  .card--front-dark { left: 40px; top: 79px; }
  .card--front-light { left: 629px; top: 79px; }
  .card--back-light { left: 40px; top: 398px; }
  .card--back-dark { left: 629px; top: 398px; }

  .swoosh { position: absolute; inset: 0; width: 100%; height: 100%; }

  .brand {
    position: absolute;
    left: 0; right: 0;
    display: flex;
    align-items: center;
    justify-content: center;
    gap: 12px;
  }
  .brand__dot {
    width: 30px; height: 30px; border-radius: 50%;
    background: var(--brand-green);
  }
  .brand__name {
    font-weight: 700;
    font-size: 34px;
    letter-spacing: 0.5px;
    color: var(--brand-blue);
  }
  .card--dark .brand__name { color: var(--brand-teal); }
  .card--front-dark .brand, .card--front-light .brand { top: 48px; }
  .card--back-light .brand, .card--back-dark .brand { top: 100px; }
  .card--back-light .brand__name, .card--back-dark .brand__name { font-size: 40px; }

  .contact {
    position: absolute;
    left: 0; right: 0;
    top: 148px;
    text-align: center;
  }
  .contact__name {
    font-weight: 700;
    font-size: 16px;
    margin-bottom: 10px;
  }
  .contact__role { font-weight: 400; font-size: 13px; }
  .contact__line {
    font-size: 11.5px;
    line-height: 19px;
  }
  .contact__line b { font-weight: 700; }

  .website {
    position: absolute;
    left: 0; right: 0;
    bottom: 30px;
    text-align: center;
    font-size: 15px;
    font-weight: 600;
    letter-spacing: 1px;
  }
</style>
</head>
<body>

  <section class="card card--dark card--front-dark">
    <svg class="swoosh" viewBox="0 0 532 290" aria-hidden="true">
      <path d="M340 0 C420 20 480 40 532 90 L532 60 C490 30 440 10 400 0 Z" fill="var(--brand-blue)"/>
      <path d="M400 0 C450 10 500 30 532 60 L532 0 Z" fill="var(--brand-green)"/>
      <path d="M0 190 C40 250 120 280 220 290 L160 290 C90 280 30 250 0 215 Z" fill="var(--brand-blue)"/>
      <path d="M0 215 C30 250 90 280 160 290 L0 290 Z" fill="var(--brand-green)"/>
    </svg>
    <div class="brand"><span class="brand__dot"></span><span class="brand__name">BLUE LEDGER PLUS</span></div>
    <div class="contact">
      <p class="contact__name">DENNIS HOLTBERG <span class="contact__role">- Manger</span></p>
      <p class="contact__line"><b>p :</b> 5550148822 &nbsp;|&nbsp; <b>f :</b> 5550193377 &nbsp;|&nbsp; <b>tf :</b> 5550193377</p>
      <p class="contact__line"><b>e :</b> BlueLEDGERPLUS@mailnook.example &nbsp;|&nbsp; <b>w :</b> BLUELEDGERPLUS.example</p>
      <p class="contact__line">3710 S Wexford st 204, Ashcombe GA 30999</p>
    </div>
  </section>

  <section class="card card--light card--front-light">
    <svg class="swoosh" viewBox="0 0 532 290" aria-hidden="true">
      <path d="M340 0 C420 20 480 40 532 90 L532 60 C490 30 440 10 400 0 Z" fill="var(--brand-blue)"/>
      <path d="M400 0 C450 10 500 30 532 60 L532 0 Z" fill="var(--brand-green)"/>
      <path d="M0 190 C40 250 120 280 220 290 L160 290 C90 280 30 250 0 215 Z" fill="var(--brand-blue)"/>
      <path d="M0 215 C30 250 90 280 160 290 L0 290 Z" fill="var(--brand-green)"/>
    </svg>
    <div class="brand"><span class="brand__dot"></span><span class="brand__name">BLUE LEDGER PLUS</span></div>
    <div class="contact">
      <p class="contact__name">HAROLD QUINCE <span class="contact__role">- Manger</span></p>
      <p class="contact__line"><b>p :</b> 5550148822 &nbsp;|&nbsp; <b>f :</b> 5550193377 &nbsp;|&nbsp; <b>tf :</b> 5550193377</p>
      <p class="contact__line"><b>e :</b> BlueLEDGERPLUS@mailnook.example &nbsp;|&nbsp; <b>w :</b> BLUELEDGERPLUS.example</p>
      <p class="contact__line">3710 S Wexford st 204, Ashcombe GA 30999</p>
    </div>
  </section>

  <section class="card card--light card--back-light">
    <div class="brand"><span class="brand__dot"></span><span class="brand__name">BLUE LEDGER PLUS</span></div>
    <p class="website">www.BLUELEDGERPLUS.example</p>
  </section>

  <section class="card card--dark card--back-dark">
    <div class="brand"><span class="brand__dot"></span><span class="brand__name">BLUE LEDGER PLUS</span></div>
    <p class="website">www.BLUELEDGERPLUS.example</p>
  </section>

</body>
</html>
```